BrambleWare business card

Looking for business card design that supports our company/software values. We have 2 logo designs at the moment but open to change if you think you can enhance the brand. Check out website www.brambleware.com.au.

Target Market(s)

Education

Contact Information for Business Card

Name, title, mobile, email and website

Font styles to use
Sans Serif

Colors

Designer to choose colors to be used in the design.

Requirements
Must have
• BrambleWare logo with tree and tagline on rear side with dark grey background colour

```html
<!DOCTYPE html>
<html lang="en">
<head>
<meta charset="utf-8">
<title>BrambleWare business card</title>
<link rel="stylesheet" href="https://fonts.googleapis.com/css2?family=Open+Sans:wght@400;600;700&display=swap">
<style>
  :root {
    --backdrop: #d3d3d3;
    --card-dark: #505050;
    --card-light: #ffffff;
    --brand-green: #3a6b35;
    --ink-grey: #4a4a4a;
    --stripe-grey: #555555;
    --white: #ffffff;
  }
  * { margin: 0; padding: 0; box-sizing: border-box; }
  html, body {
    width: 1200px; height: 852px; overflow: hidden;
    background: var(--backdrop);
    font-family: "Open Sans", Arial, sans-serif;
  }
  .canvas { position: relative; width: 1200px; height: 852px; }
  .card {
    position: absolute; width: 520px; height: 298px;
    border-radius: 22px; overflow: hidden;
    box-shadow: 0 6px 14px rgba(0,0,0,0.25);
  }
  .card-back { left: 70px; top: 110px; background: var(--card-dark); }
  .card-front { left: 610px; top: 440px; background: var(--card-light); }

  .brand { position: absolute; display: flex; flex-direction: column; }
  .brand-row { display: flex; align-items: center; gap: 12px; }
  .brand-dot { border-radius: 50%; flex: none; }
  .brand-name { font-weight: 400; line-height: 1; letter-spacing: 0.5px; }
  .brand-tagline { border-top: 1px solid; padding-top: 3px; margin-top: 5px; }

  .card-back .brand { left: 130px; top: 108px; color: var(--white); }
  .card-back .brand-dot { width: 46px; height: 46px; background: var(--white); }
  .card-back .brand-name { font-size: 40px; }
  .card-back .brand-tagline { font-size: 15px; margin-left: 58px; border-color: var(--white); }

  .card-front .brand { right: 28px; top: 34px; color: var(--ink-grey); }
  .card-front .brand-dot { width: 30px; height: 30px; background: var(--brand-green); }
  .card-front .brand-name { font-size: 26px; }
  .card-front .brand-tagline { font-size: 10px; margin-left: 42px; border-color: var(--ink-grey); }

  .swoosh { position: absolute; inset: 0; }
  .person { position: absolute; left: 36px; top: 118px; }
  .person-name { font-size: 17px; font-weight: 700; color: var(--brand-green); letter-spacing: 0.5px; }
  .person-title { font-size: 15px; color: var(--ink-grey); margin-top: 2px; }
  .contacts { position: absolute; left: 36px; top: 196px; list-style: none; }
  .contacts li {
    display: flex; align-items: center; gap: 10px;
    font-size: 14px; color: var(--ink-grey); line-height: 24px;
  }
  .contacts svg { width: 12px; height: 12px; fill: var(--brand-green); flex: none; }
</style>
</head>
<body>
<main class="canvas">
  <section class="card card-back" aria-label="Card back">
    <div class="brand">
      <div class="brand-row">
        <span class="brand-dot"></span>
        <span class="brand-name">BrambleWare</span>
      </div>
      <span class="brand-tagline">Student Success Platform</span>
    </div>
  </section>

  <section class="card card-front" aria-label="Card front">
    <svg class="swoosh" viewBox="0 0 520 298" preserveAspectRatio="none" aria-hidden="true">
      <path d="M150 298 C300 270 430 200 520 110 L520 298 Z" fill="var(--stripe-grey)"/>
      <path d="M170 298 C320 272 440 210 520 124 L520 298 Z" fill="var(--white)"/>
      <path d="M200 298 C340 276 450 220 520 140 L520 298 Z" fill="var(--brand-green)"/>
    </svg>
    <div class="brand">
      <div class="brand-row">
        <span class="brand-dot"></span>
        <span class="brand-name">BrambleWare</span>
      </div>
      <span class="brand-tagline">Student Success Platform</span>
    </div>
    <div class="person">
      <p class="person-name">TOMAS REED</p>
      <p class="person-title">Doctor</p>
    </div>
    <ul class="contacts">
      <li>
        <svg viewBox="0 0 24 24"><path d="M6.6 10.8a15.1 15.1 0 0 0 6.6 6.6l2.2-2.2a1 1 0 0 1 1-.25 11.4 11.4 0 0 0 3.6.57 1 1 0 0 1 1 1V20a1 1 0 0 1-1 1A17 17 0 0 1 3 4a1 1 0 0 1 1-1h3.5a1 1 0 0 1 1 1c0 1.25.2 2.45.57 3.57a1 1 0 0 1-.25 1z"/></svg>
        555-014-2287
      </li>
      <li>
        <svg viewBox="0 0 24 24"><path d="M2 5h20v14H2z M4 7v1l8 5 8-5V7l-8 5z" fill-rule="evenodd"/></svg>
        info@brambleware.com.au
      </li>
      <li>
        <svg viewBox="0 0 24 24"><circle cx="12" cy="12" r="10"/></svg>
        www.brambleware.com.au
      </li>
    </ul>
  </section>
</main>
</body>
</html>
```